A5 flyer recto (just the front side) announcing the summer events

For a public aquarium in France, we invite you to create our A5 flyer recto (just the front side) announcing the events of this summer 2015
The flyer must be written in french, you will find attached all the text that you have to fill in the flyer.
You also have to use our logo in the top or in the bottom of the flyer (2 versions of the logo four color or black and white version. According your design you can use one of them)
We also have a mascot ( a sea horse), you can use it if you want to illustrate your design (attachment file)
We manage a mini-golf and we want to promote it with a special discount, you have to mentioned this benefit in the flyer as a special discount coupon)
You must specify our website and our adress..
We remain at your disposal for any question

```html
<!DOCTYPE html>
<html lang="fr">
<head>
<meta charset="utf-8">
<title>Aquarium des Brisants – Été 2015</title>
<link rel="stylesheet" href="https://fonts.googleapis.com/css2?family=Didact+Gothic&family=Montserrat:wght@600;700&display=swap">
<style>
  :root{
    --sand-light:#f6dcc0;
    --sand:#eab585;
    --sand-deep:#dd9b5c;
    --orange:#f18a4f;
    --lime:#b5d256;
    --sky:#14a9e6;
    --magenta:#b51f78;
    --coupon-top:#f08a1e;
    --coupon-bottom:#c65417;
    --logo-green:#3f7d2a;
    --white:#ffffff;
    --note:#f6e6d6;
    --red:#c0281a;
  }
  *{margin:0;padding:0;box-sizing:border-box}
  html,body{width:846px;height:1200px;overflow:hidden}
  body{
    position:relative;
    background:linear-gradient(180deg,var(--sand-light) 0%,var(--sand) 45%,var(--sand-deep) 100%);
    font-family:"Didact Gothic",sans-serif;
    color:var(--white);
  }
  .abs{position:absolute}
  strong{font-family:"Montserrat",sans-serif;font-weight:700;text-transform:uppercase}

  .hero-art{left:0;top:0;width:846px;height:360px}
  .brand{left:70px;top:205px;display:flex;align-items:center;gap:16px}
  .brand-dot{width:38px;height:38px;border-radius:50%;background:var(--logo-green)}
  .brand-name{font-family:"Montserrat",sans-serif;font-weight:700;color:var(--logo-green);font-size:58px;line-height:1;letter-spacing:-1px}

  .band-daily{
    left:58px;top:408px;width:724px;height:122px;
    background:var(--orange);
    transform:rotate(-7deg);transform-origin:left top;
    padding:10px 14px;font-size:22px;line-height:1.3;
  }
  .band-daily strong{font-size:19px}

  .arrow-bands{left:0;top:0;width:846px;height:1200px}
  .nights{right:18px;top:506px;width:640px;text-align:right;font-size:19px;line-height:25px}
  .workshops{left:14px;top:636px;width:600px;font-size:19px;line-height:26px}

  .band-expo{
    left:234px;top:712px;width:562px;height:138px;
    background:var(--magenta);
    transform:rotate(-16deg);transform-origin:center;
    padding:10px 16px;text-align:right;font-size:19px;line-height:28px;
  }

  .coupon{left:0;top:948px;width:846px;height:86px;background:linear-gradient(180deg,var(--coupon-top),var(--coupon-bottom))}
  .mascot{left:28px;top:790px;width:120px;height:400px}
  .coupon-offer{left:0;top:958px;width:846px;text-align:center;font-family:"Montserrat",sans-serif;font-weight:700;font-size:17.5px;line-height:1.35;padding-left:110px}
  .coupon-note{left:240px;top:1014px;font-size:14px;color:var(--note)}
  .info{left:110px;top:1060px;font-family:"Montserrat",sans-serif;font-weight:700;font-size:13.5px}
  .site{left:272px;top:1084px;font-family:"Montserrat",sans-serif;font-weight:700;font-size:26px}
  .address{left:188px;top:1127px;font-family:"Montserrat",sans-serif;font-weight:600;font-size:14.5px;color:var(--red)}
  .phone{left:292px;top:1150px;font-family:"Montserrat",sans-serif;font-weight:700;font-size:30px;color:var(--red);letter-spacing:1px}
</style>
</head>
<body>

<svg class="abs hero-art" viewBox="0 0 846 360" role="img" aria-label="Photo de deux adolescentes joyeuses levant le pouce devant des ballons colorés">
  <defs>
    <linearGradient id="heroFill" x1="0" y1="0" x2="1" y2="1">
      <stop offset="0" stop-color="#f3a27a"/>
      <stop offset="0.45" stop-color="#f6c66a"/>
      <stop offset="0.8" stop-color="#f0a0b0"/>
      <stop offset="1" stop-color="#f5c08a"/>
    </linearGradient>
  </defs>
  <path d="M0 0H846V215C700 250 560 300 430 320C300 340 160 300 0 250Z" fill="url(#heroFill)"/>
</svg>

<div class="abs brand">
  <span class="brand-dot"></span>
  <span class="brand-name">Aquarium<br>des Brisants</span>
</div>

<div class="abs band-daily"><strong>Tous les jours, animations « bassin tactile » commentées.</strong><br>Tous les après-midis Nourrissages commentés de nos<br>espèces aquatiques.</div>

<svg class="abs arrow-bands" viewBox="0 0 846 1200" aria-hidden="true">
  <polygon points="292,502 846,500 846,632 238,619 160,578" fill="var(--lime)"/>
  <polygon points="0,630 572,630 622,682 560,750 0,750" fill="var(--sky)"/>
</svg>

<div class="abs nights">Les mardis 21 &amp; 28 juillet, 4 &amp; 11 août de 20h à 23h, les<br><strong>Nocturnes de l’aquarium,</strong> avis de tempête.<br>Découvrez l’Aquarium des Brisants comme vous ne l’avez jamais<br>visité. 4 comédiens investissent l’aquarium pour une visite<br>drôle et décalée à faire en famille.</div>

<div class="abs workshops">Les jeudis 9 &amp; 16 juillet, 20 &amp; 27 août de 14h à 17h pour<br>les enfants de 6 à 12 ans, l’aquarium propose des<br><strong>Ateliers scientifiques</strong>. En compagnie d’un animateur,<br>l’occasion d’apprendre en s’amusant.</div>

<div class="abs band-expo">En juillet &amp; août, <strong>Exposition</strong> « Laisse de Mer, source de<br>vie » de Margot Lestrade.<br>Mieux comprendre la laisse de mer, son rôle écologique,<br>son utilité pour nos plages…</div>

<div class="abs coupon"></div>

<svg class="abs mascot" viewBox="0 0 120 400" role="img" aria-label="Mascotte hippocampe vert souriant">
  <ellipse cx="60" cy="385" rx="55" ry="10" fill="#b8834f" opacity="0.6"/>
  <rect x="10" y="0" width="100" height="372" rx="50" fill="#a9cc4a" opacity="0.85"/>
</svg>

<div class="abs coupon-offer">Sur présentation de ce coupon, bénéficiez d’une partie mini-golf<br>enfant offerte pour une partie mini-golf adulte achetée *</div>
<div class="abs coupon-note">*offre non cumulable avec toute autre promotion</div>

<div class="abs info">Retrouvez toutes les informations, tarif, horaires et conditions d’inscriptions sur :</div>
<div class="abs site">aquariumdesbrisants.fr</div>
<div class="abs address">Aquarium des Brisants&nbsp; 14, rue des Goélands 56000 VANNES</div>
<div class="abs phone">02 97 00 12 34</div>

</body>
</html>
```